Academic and Business book cover

I need a book cover for my academic and business book.
The focus is in international / global negotiation and influence (how to negotiate across cultures).
The book will be published on Torvex, both in Vellor and printed edition. therefore I need something that works under Torvex guidelines.The final design should be elegant and still be able to stand out against the competition.
I would like to have orange+grey for the text colors on the cover, even if different options are welcome.
Title and my name are in the attached word doc.

Target Market(s)

graduates, Phds, from international business schools. Managers

Industry/Entity Type

Business

Font styles to use
Serif
Sans Serif

Colors

Designer to choose colors to be used in the design.

Requirements
Must have
• The title and my name should have elegant fonts.
Nice to have
• pictures of the world that don't have the "usual" Europe in the centre.

```html
<!DOCTYPE html>
<html lang="en">
<head>
<meta charset="utf-8">
<title>The 3Cs Blueprint – Book Cover Spread</title>
<link rel="stylesheet" href="https://fonts.googleapis.com/css2?family=Alfa+Slab+One&family=Oswald:wght@300;400&family=Roboto:wght@300;400&display=swap">
<style>
  :root {
    --page-bg: #ffffff;
    --sky-top: #ffffff;
    --sky-pale: #d3f0fb;
    --sky-mid: #5cc6ee;
    --sky-deep: #1ea3df;
    --sky-low: #a6def4;
    --ink-dark: #141414;
    --ink-navy: #0b2a4a;
    --ink-body: #1d2a33;
    --map-land: #f2faff;
    --map-shade: #1c64a8;
    --isbn-box: #ffffff;
  }
  * { box-sizing: border-box; margin: 0; padding: 0; }
  html, body {
    width: 1200px; height: 857px; overflow: hidden;
    background: var(--page-bg);
  }
  .cover-spread {
    position: absolute; left: 96px; top: 77px;
    width: 1023px; height: 753px;
    display: flex;
  }
  .back-cover {
    position: relative; width: 502px; height: 100%;
    background: linear-gradient(180deg, var(--sky-top) 0%, var(--sky-pale) 14%, var(--sky-mid) 38%, var(--sky-deep) 50%, var(--sky-mid) 64%, var(--sky-low) 84%, var(--sky-top) 100%);
    font-family: "Roboto", Arial, sans-serif;
    font-weight: 300;
    color: var(--ink-body);
  }
  .spine {
    position: relative; width: 19px; height: 100%;
    background: linear-gradient(180deg, var(--sky-top) 0%, var(--sky-pale) 18%, var(--sky-mid) 48%, var(--sky-low) 82%, var(--sky-top) 100%);
    font-family: "Oswald", "Arial Narrow", sans-serif;
    color: var(--ink-dark);
  }
  .front-cover {
    position: relative; width: 502px; height: 100%;
    background: linear-gradient(180deg, var(--sky-top) 0%, var(--sky-pale) 18%, var(--sky-mid) 48%, var(--sky-deep) 60%, var(--sky-mid) 72%, var(--sky-low) 88%, var(--sky-top) 100%);
    text-align: center;
  }

  .back-imprint { position: absolute; left: 0; top: 42px; padding-left: 0; font-size: 14px; line-height: 18px; }
  .back-title { position: absolute; left: 0; top: 82px; width: 470px; font-size: 13px; line-height: 21px; }
  .copyright-block {
    position: absolute; right: 11px; top: 525px;
    text-align: right; font-size: 12px; line-height: 20px;
  }
  .publisher-line { position: absolute; right: 11px; top: 572px; font-size: 12px; line-height: 20px; }
  .isbn-box {
    position: absolute; left: 291px; top: 610px; width: 202px; height: 65px;
    background: var(--isbn-box);
    font-family: "Times New Roman", Times, serif; font-size: 13px; font-weight: 400;
    text-align: center; padding-top: 8px; color: var(--ink-dark);
  }
  .cataloging-line { position: absolute; left: 190px; top: 699px; font-size: 12px; line-height: 20px; }

  .spine-title, .spine-author {
    position: absolute; left: 0; width: 19px;
    writing-mode: vertical-rl;
    display: flex; align-items: center; justify-content: center;
    font-size: 13px; line-height: 19px; letter-spacing: 0.3px; white-space: nowrap;
  }
  .spine-title { top: 30px; }
  .spine-author { top: 625px; font-weight: 300; }

  .book-title {
    position: absolute; left: 0; right: 0; top: 38px;
    font-family: "Alfa Slab One", Georgia, serif; font-weight: 400;
    font-size: 32px; line-height: 40px; letter-spacing: 1px;
    white-space: nowrap; color: var(--ink-dark);
    transform: scaleY(1.3);
  }
  .book-subtitle {
    position: absolute; left: 0; right: 0; top: 94px;
    font-family: "Oswald", "Arial Narrow", sans-serif; font-weight: 300;
    font-size: 21px; line-height: 28px; color: var(--ink-navy);
    white-space: nowrap;
  }
  .world-map {
    position: absolute; left: 0; top: 185px; width: 502px; height: 369px;
    background: radial-gradient(ellipse 60% 50% at 50% 48%, var(--map-land) 0%, rgba(242,250,255,0.75) 45%, rgba(28,100,168,0.35) 80%, rgba(28,100,168,0) 100%);
  }
  .author-name {
    position: absolute; left: 0; right: 0; top: 699px;
    font-family: "Oswald", "Arial Narrow", sans-serif; font-weight: 300;
    font-size: 16px; line-height: 20px; color: var(--ink-body);
  }
</style>
</head>
<body>
  <main class="cover-spread">
    <section class="back-cover">
      <p class="back-imprint">Halvern Press – Self Published Book</p>
      <p class="back-title">The 3Cs Blueprint: Applied Negotiation and Persuasion Methods<br>for Cross-Cultural Success</p>
      <div class="copyright-block">
        <p>Copyright © 2013 by Darshan K. Mehra</p>
        <p>All Rights Reserved</p>
      </div>
      <p class="publisher-line">Published in the United States by Halvern Press</p>
      <div class="isbn-box">ISBN</div>
      <p class="cataloging-line">Library of Congress Cataloging in Publication Data</p>
    </section>
    <section class="spine">
      <p class="spine-title">THE 3CS BLUEPRINT</p>
      <p class="spine-author">Darshan K. Mehra</p>
    </section>
    <section class="front-cover">
      <h1 class="book-title">THE 3CS BLUEPRINT</h1>
      <h2 class="book-subtitle">APPLIED NEGOTIATION AND PERSUASION METHODS<br>FOR CROSS-CULTURAL SUCCESS</h2>
      <div class="world-map" role="img" aria-label="World map with white and dark blue continents over a faint grid"></div>
      <p class="author-name">Darshan K. Mehra</p>
    </section>
  </main>
</body>
</html>
```